Timeline flyer

Hi, we are an agency, our business is to orienteates student to study abroad in Germany. For that, we enroll them in language schools in Germany and help them to find an accomodation.
Students are always lost we thinked about a timeline to help them figure out what they have to do once in Germany so they don't miss delays.
You can find in the attachement an example that i made in powerpoint but it's really basic and it's only for u so you can understant what the timeline should look like.
We need two time lines.
For the first one (file first timeline)
Title : Procédure pour intégrer le semestre d’hiver dans les universités Allemandes
The first paragraph (up on the left in my proposition) : L’étudiant devra pendant ces mois débuter ses cours d’allemand en Tunisie et les poursuivre en Allemagne après l’obtention du Visa d’étude. L’atteinte du niveau C1 est primordiale pour la bonne réussite du test Kel ou le PLQ.
The second paragraph (below on the left in my proposition) : L’étudiant devra à cette date avoir déjà passer le test KEL ou le PLQ pour pouvoir être à temps pour les inscriptions universitaires. Il faut compter 6 semaines pour le test Kel et 2 à 3 semaines pour obtenir les résultats des tests.
The third one (up on the right in my proposition) : Le dernier délais d’inscription pour pouvoir intégrer une université Allemande pendant la rentrée hivernale (15 Octobre).
The last one (below on the right in my proposition) : Rentrée universitaire
For the second one (file second timeline) :
Title : Procédure pour intégrer le semestre d’été dans les universités Allemandes *
The third one (up on the right in my proposition) : Le dernier délais d’inscription pour pouvoir intégrer une université Allemande pendant la rentrée estivale (15 Avril).
There is also an additional sentence below in the right for this one : * Les spécialités assurées pendant les semestres d’été sont limitées.
You can also find in the attachement our flyers (so you can inspire youself with the color and the design), we want our student to recognize that the flyer is related to our agency so please try to use colors that are matched with the other flyer.
Also, you can find our Logo in the attachement.
Thank you :)
Waiting for your propositions ! :)

```html
<!DOCTYPE html>
<html lang="fr">
<head>
<meta charset="utf-8">
<title>Procédure pour intégrer le semestre d'hiver</title>
<link href="https://fonts.googleapis.com/css2?family=Oswald:wght@500&family=Roboto+Condensed:wght@700&family=PT+Sans:wght@400&display=swap" rel="stylesheet">
<style>
  :root{
    --olive:#9d9a2e;
    --olive-text:#999432;
    --lime:#d3dc1f;
    --teal:#4ec4c9;
    --grey-line:#c9c9c9;
    --grey-band:#c7c7c7;
    --ink:#222;
    --paper:#fff;
  }
  *{box-sizing:border-box;margin:0;padding:0}
  html,body{width:1200px;height:846px;overflow:hidden;background:var(--paper)}
  .flyer{position:relative;width:1200px;height:846px;overflow:hidden;background:var(--paper);font-family:"PT Sans",sans-serif;color:var(--ink)}
  .decor{position:absolute;inset:0}
  .title{position:absolute;left:228px;top:22px;font-family:"Oswald",sans-serif;font-weight:500;font-size:27px;letter-spacing:.2px;color:var(--paper);white-space:nowrap}
  .note{position:absolute;border:3px solid var(--lime);background:var(--paper);font-size:14.5px;line-height:1.42;text-align:center;display:flex;align-items:center;justify-content:center;padding:6px 14px}
  .note--language{left:227px;top:131px;width:503px;height:96px}
  .note--deadline{left:749px;top:131px;width:294px;height:96px}
  .note--opening{left:766px;top:258px;width:121px;height:91px;line-height:1.3;padding:4px}
  .note--tests{left:564px;top:605px;width:398px;height:119px;padding:6px 16px}
  .date{position:absolute;width:130px;margin-left:-65px;text-align:center;font-family:"Roboto Condensed",sans-serif;font-weight:700;font-size:18px;line-height:1.2;color:var(--olive-text)}
  .date span{display:block}
  .date--up .year{font-size:20px}
  .date--down .year{font-size:20px}
  .date--up{top:377px}
  .date--down{top:508px}
  .brand{position:absolute;left:34px;top:418px;font-family:"Roboto Condensed",sans-serif;font-weight:700;font-size:50px;line-height:1;color:#3a3a3a;letter-spacing:-1px}
  .mascot{position:absolute;left:112px;top:565px;width:146px;height:200px;border-radius:40% 40% 30% 30%;background:linear-gradient(180deg,#3b3b3b 0 18%,#f2f4f7 18%,#dfe6ee 100%)}
  .contact{position:absolute;top:803px;display:flex;align-items:center;gap:8px;font-size:13px;color:var(--ink)}
  .contact svg{width:14px;height:14px}
  .contact--tunis{left:208px}
  .contact--sfax{left:400px}
  .contact--sousse{left:580px}
  .contact--web{left:880px}
  .contact--social{left:1072px}
  .dot{width:12px;height:12px;border-radius:50%;background:#333}
</style>
</head>
<body>
<main class="flyer">
  <svg class="decor" width="1200" height="846" viewBox="0 0 1200 846">
    <!-- header -->
    <polygon points="0,0 185,0 130,60 0,60" fill="var(--lime)"/>
    <polygon points="0,0 140,0 95,40 0,40" fill="var(--teal)" opacity=".0"/>
    <polygon points="185,0 1200,0 1200,15 175,15" fill="var(--lime)"/>
    <polygon points="200,8 1200,8 1200,70 150,70" fill="var(--olive)"/>
    <polygon points="1080,0 1200,0 1200,36 1055,36" fill="var(--teal)"/>
    <polygon points="0,0 60,0 0,38" fill="var(--teal)"/>
    <!-- connectors -->
    <g stroke="var(--lime)" stroke-width="3" fill="none">
      <line x1="486" y1="227" x2="486" y2="310"/>
      <polyline points="244,462 244,310 696,310 696,365"/>
      <line x1="892" y1="227" x2="892" y2="462"/>
      <line x1="827" y1="349" x2="827" y2="368"/>
      <line x1="761" y1="482" x2="761" y2="605"/>
    </g>
    <g fill="var(--olive)">
      <circle cx="486" cy="310" r="4.5"/>
      <circle cx="244" cy="310" r="4.5"/>
      <circle cx="696" cy="365" r="4.5"/>
      <circle cx="827" cy="368" r="4.5"/>
      <circle cx="761" cy="567" r="4.5"/>
    </g>
    <!-- timeline -->
    <line x1="244" y1="471" x2="1160" y2="471" stroke="var(--grey-line)" stroke-width="5"/>
    <polygon points="1150,459 1178,471 1150,483" fill="var(--grey-line)"/>
    <g fill="var(--paper)" stroke="#c8cf3a" stroke-width="3">
      <circle cx="244" cy="471" r="7"/><circle cx="308" cy="471" r="7"/>
      <circle cx="373" cy="471" r="7"/><circle cx="437" cy="471" r="7"/>
      <circle cx="502" cy="471" r="7"/><circle cx="567" cy="471" r="7"/>
      <circle cx="632" cy="471" r="7"/><circle cx="696" cy="471" r="7"/>
      <circle cx="761" cy="471" r="7"/><circle cx="827" cy="471" r="7"/>
      <circle cx="892" cy="471" r="7"/><circle cx="957" cy="471" r="7"/>
      <circle cx="1021" cy="471" r="7"/><circle cx="1086" cy="471" r="7"/>
    </g>
    <!-- footer -->
    <polygon points="0,738 1200,738 1200,780 0,780" fill="var(--lime)" opacity=".0"/>
    <polygon points="0,738 820,738 790,776 0,776" fill="var(--lime)"/>
    <polygon points="0,786 1200,786 1200,846 0,846" fill="var(--lime)"/>
    <polygon points="840,786 1200,786 1200,846 810,846" fill="var(--grey-band)"/>
  </svg>

  <h1 class="title">PROCÉDURE POUR INTÉGRER LE SEMESTRE D’HIVER DANS LES UNIVERSITÉS ALLEMANDES</h1>

  <p class="note note--language">L’étudiant devra pendant ces mois débuter ses cours d’allemand en Tunisie et les poursuivre en Allemagne après l’obtention du Visa d’étude. L’atteinte du niveau C1 est primordiale pour la bonne réussite du test Kel ou le PLQ.</p>
  <p class="note note--deadline">Fin des inscriptions universitaires</p>
  <p class="note note--opening">Début des inscriptions à l’université</p>
  <p class="note note--tests">L’étudiant devra à cette date avoir déjà passer le test KEL ou le PLQ pour pouvoir être à temps pour les inscriptions universitaires. Il faut compter 6 semaines pour le test Kel et 2 à 3 semaines pour obtenir les résultats des tests.</p>

  <div class="date date--up" style="left:308px"><span>Oct</span><span class="year">2016</span></div>
  <div class="date date--up" style="left:437px"><span>Déc</span><span class="year">2016</span></div>
  <div class="date date--up" style="left:567px"><span>Fév</span><span class="year">2017</span></div>
  <div class="date date--up" style="left:696px"><span>Avr</span><span class="year">2017</span></div>
  <div class="date date--up" style="left:827px"><span>15 Juin</span><span class="year">2017</span></div>
  <div class="date date--up" style="left:957px"><span>Août</span><span class="year">2017</span></div>
  <div class="date date--up" style="left:1086px"><span>15 Octobre</span><span class="year">2017</span></div>

  <div class="date date--down" style="left:244px"><span class="year">2016</span><span>Sep</span></div>
  <div class="date date--down" style="left:373px"><span class="year">2016</span><span>Nov</span></div>
  <div class="date date--down" style="left:502px"><span class="year">2017</span><span>Jan</span></div>
  <div class="date date--down" style="left:632px"><span class="year">2017</span><span>Mars</span></div>
  <div class="date date--down" style="left:761px"><span class="year">2017</span><span>Début Mai</span></div>
  <div class="date date--down" style="left:892px"><span class="year">2017</span><span>15 Juillet</span></div>
  <div class="date date--down" style="left:1021px"><span class="year">2017</span><span>Sep</span></div>
  <div class="date date--down" style="left:1150px"><span class="year">2017</span><span>Nov</span></div>

  <div class="brand">studora</div>

  <div class="mascot" role="img" aria-label="Illustration d’un bonhomme de neige avec chapeau haut-de-forme, écharpe et skis"></div>

  <div class="contact contact--tunis"><svg viewBox="0 0 16 16"><path d="M3 1h3l1.5 4-2 1.2a9 9 0 0 0 4.3 4.3L11 8.5l4 1.5v3a2 2 0 0 1-2 2A12 12 0 0 1 1 3a2 2 0 0 1 2-2z" fill="#222"/></svg>Tunis: 71 000 481</div>
  <div class="contact contact--sfax"><svg viewBox="0 0 16 16"><path d="M3 1h3l1.5 4-2 1.2a9 9 0 0 0 4.3 4.3L11 8.5l4 1.5v3a2 2 0 0 1-2 2A12 12 0 0 1 1 3a2 2 0 0 1 2-2z" fill="#222"/></svg>Sfax 74 000 562</div>
  <div class="contact contact--sousse"><svg viewBox="0 0 16 16"><path d="M3 1h3l1.5 4-2 1.2a9 9 0 0 0 4.3 4.3L11 8.5l4 1.5v3a2 2 0 0 1-2 2A12 12 0 0 1 1 3a2 2 0 0 1 2-2z" fill="#222"/></svg>Sousse 73 000 915</div>
  <div class="contact contact--web"><span class="dot"></span>www.studora.org</div>
  <div class="contact contact--social"><span class="dot"></span>STUDORA</div>
</main>
</body>
</html>
```